Kaffeerösterei sucht Etiketten-Design
- schnelle Ausführung - mein Geschmack voll getroffen - unkompliziert und Kunden orientiert bei der Ausführung
Zielgruppe
Kaffeerösterei für die edelsten und teuersten Rohkaffees.
Meine Kunden sind Kaffee Geniesser.
Aufgabenstellung
Transparente Aufkleber für eine Schiefertafel im Format 22.5 cm x 15.5 cm.
Im Hand-Lettering Stil.
5 Schiefertafeln sind gewünscht.
Tafel 1
Kostenlos zur Degustation
Espresso
Café Crème 3.--
Americano 3.--
Filter Kaffee 3.--
Tafel 2
Kaffee & Milch
Cappuccino 4.--
Café Latte 4.--
Flat White 4.--
Latte Macchiato 4.--
Latte Macchiato mit Aroma 5.--
Kaffee & Hafermilch + 1.--
Tafel 3
Crepes
Pikant
- Pizza Crepes 7.--
- Flammkuchen Crepes 7.--
Süss
- Schoggi Crepes 6.--
- Apfelmus & Zimtzucker 6.--
Tafel 4
Kaffee & Schnaps
- Original Entlebucher Schwarzes 7.--
- Espresso Coretto 5.00
- Schwarzes mit Rahmhaube 8.--
Tafel 5
Schokolade & Milch
- heisse Schoggi 5.--
- heisse Schoggi mit Rahmhaube 6.--
- heisse Schoggi mit Espresso 6.--
- Schokolade & Hafermilch +1.--
Als Idee, was mir gefallen könnte:
https://www.bildsammlung.example/pin/551203948817265034/
https://de.grafikquelle.example/vektorkunst/4182093-set-kaffeekarte-mit-tassen-kaffeegetranken-im-vintage-stil-stilisierte-zeichnung-mit-kreide-auf-tafel-schriftzug-know-your-coffee
https://www.fotoarchiv.example/stockfoto-heisser-kakao-bar-warm-hier-oben-hand-tafel-caf-schild-an-tafel-hintergrund-mit-farbe-kreide-schriftzug-werbung-fur-heisse-d-837215406.html

```html
<!DOCTYPE html>
<html lang="de">
<head>
<meta charset="utf-8">
<title>Tafel 1 – Kostenlos zur Degustation</title>
<link rel="stylesheet" href="https://fonts.googleapis.com/css2?family=Amatic+SC:wght@700&family=Kaushan+Script&display=swap">
<style>
  :root {
    --paper: #ffffff;
    --slate: #1d1d1b;
    --chalk: #ffffff;
    --honey: #f9cf72;
    --cream: #fdebd0;
    --sage: #d1dd9c;
    --blush: #e4937a;
  }
  * { margin: 0; padding: 0; box-sizing: border-box; }
  html, body {
    width: 1200px; height: 874px; overflow: hidden;
    background: var(--paper);
  }
  .slate {
    position: absolute;
    left: 62px; top: 64px;
    width: 1077px; height: 742px;
    background: var(--slate);
  }
  .headline {
    position: absolute;
    left: 0; right: 0; top: 138px;
    text-align: center;
    font-family: "Amatic SC", cursive;
    font-weight: 700;
    font-size: 84px;
    line-height: 1;
    color: var(--honey);
    letter-spacing: 1px;
  }
  .title {
    position: absolute;
    left: 0; right: 0; top: 214px;
    text-align: center;
    font-family: "Kaushan Script", cursive;
    font-size: 92px;
    line-height: 1.2;
    color: var(--chalk);
  }
  .flourish {
    position: absolute;
    top: 274px;
    width: 78px; height: 44px;
    border-radius: 22px;
    background: linear-gradient(90deg, rgba(253,235,208,0.25), rgba(253,235,208,0.45));
  }
  .flourish--left { left: 298px; }
  .flourish--right { left: 824px; }
  .illustration {
    position: absolute;
    left: 135px; top: 322px;
    width: 316px; height: 366px;
    border-radius: 40px 40px 150px 150px / 40px 40px 40px 40px;
    background: linear-gradient(180deg, #2e2e2b 0%, #3a3a36 70%, var(--sage) 100%);
  }
  .menu {
    position: absolute;
    left: 0; top: 410px;
    width: 1200px;
    list-style: none;
  }
  .menu__item {
    position: relative;
    height: 90px;
    font-family: "Amatic SC", cursive;
    font-weight: 700;
    font-size: 82px;
    line-height: 90px;
  }
  .menu__name {
    position: absolute;
    right: 318px;
    color: var(--chalk);
    white-space: nowrap;
  }
  .menu__price {
    position: absolute;
    left: 906px;
    color: var(--cream);
    white-space: nowrap;
    -webkit-text-stroke: 1.5px var(--cream);
  }
  .rule {
    position: absolute;
    left: 350px; top: 722px;
    width: 490px; height: 22px;
  }
</style>
</head>
<body>
  <main class="slate-sign">
    <div class="slate"></div>

    <p class="headline">Kostenlos zur Degustation</p>

    <div class="flourish flourish--left" role="img" aria-label="Verzierung links neben dem Titel"></div>
    <h1 class="title">Espresso</h1>
    <div class="flourish flourish--right" role="img" aria-label="Verzierung rechts neben dem Titel"></div>

    <div class="illustration" role="img" aria-label="Illustration einer dampfenden Kaffeekanne auf grünem Untersetzer"></div>

    <ul class="menu">
      <li class="menu__item"><span class="menu__name">Café Crème</span><span class="menu__price">3,–</span></li>
      <li class="menu__item"><span class="menu__name">Americano</span><span class="menu__price">3,–</span></li>
      <li class="menu__item"><span class="menu__name">Filter Kaffee</span><span class="menu__price">3,–</span></li>
    </ul>

    <svg class="rule" viewBox="0 0 490 22" aria-hidden="true">
      <path d="M4 12 C 120 4, 300 2, 486 14 C 300 10, 150 10, 8 16 Z" fill="var(--honey)"/>
    </svg>
  </main>
</body>
</html>
```